Web site design for Brivolt Software (www.brivoltsoftware-example.com)

Need the design as well as the html for the website. The brief is given in the attached file.
If possible, would like to use pencil sketches instead of images to give a unique look to the site.
Target Market(s)
small Software product companies
Industry/Entity Type
Software
Coding
Coded - Design and coding required
Number of Pages Required
5+ page

```html
<!DOCTYPE html>
<html lang="en">
<head>
<meta charset="utf-8">
<title>Brivolt Software — Make Your Product Happen</title>
<link rel="stylesheet" href="https://fonts.googleapis.com/css2?family=Audiowide&family=Open+Sans:wght@400;600;700&display=swap">
<style>
:root{
  --red:#d3141b;
  --red-dark:#a80d12;
  --ink:#1d1d1f;
  --text:#555a60;
  --muted:#8a8f96;
  --white:#ffffff;
  --blush:#fbeeee;
  --footer:#1f1f21;
  --footer-line:#333338;
  --teal:#2aa6b8;
  --green:#4caf50;
  --blue:#2f6fd1;
}
*{box-sizing:border-box;margin:0;padding:0}
html,body{width:1200px;height:2960px;overflow:hidden}
body{font-family:"Open Sans",Arial,sans-serif;color:var(--text);background:var(--white);position:relative}
.display{font-family:"Audiowide","Arial Black",sans-serif;text-transform:uppercase;letter-spacing:1px}
section,header,footer{position:absolute;left:0;width:1200px}
.btn{display:inline-block;background:var(--red);color:var(--white);font-weight:700;font-size:13px;letter-spacing:.5px;text-transform:uppercase;padding:14px 26px;border-radius:3px}

/* Hero */
.hero{top:0;height:720px;background:linear-gradient(160deg,#3a3d42 0%,#1c1e22 45%,#0d0e10 100%);overflow:hidden}
.hero__image{position:absolute;inset:0;background:radial-gradient(ellipse at 62% 40%,rgba(150,155,165,.35),rgba(20,22,25,0) 60%),linear-gradient(90deg,rgba(10,10,12,.55),rgba(10,10,12,0) 60%)}
.nav{position:absolute;top:22px;left:150px;right:150px;display:flex;justify-content:space-between;align-items:center}
.brand{display:flex;align-items:center;gap:10px;color:var(--white);font-family:"Audiowide",sans-serif;font-size:30px;letter-spacing:2px}
.brand__mark{width:14px;height:14px;background:var(--red)}
.menu-toggle{width:26px;display:flex;flex-direction:column;gap:5px}
.menu-toggle span{height:3px;background:var(--white)}
.hero__title{position:absolute;left:160px;top:170px;color:var(--white);font-size:58px;line-height:66px}
.hero__lead{position:absolute;left:160px;top:322px;width:420px;color:#e4e4e4;font-size:14px;line-height:21px}
.hero .btn{position:absolute;left:160px;top:420px}
.play{position:absolute;left:1000px;top:260px;width:86px;height:86px}
.partners{position:absolute;left:0;right:0;top:640px;height:80px;background:rgba(0,0,0,.45);display:flex;align-items:center;padding:0 150px;justify-content:space-between}
.partners__text{color:var(--white);font-size:12px;font-weight:600;letter-spacing:.3px}
.partners__logos{display:flex;gap:28px;align-items:center}
.partner-badge{width:92px;height:30px;background:rgba(255,255,255,.75);border-radius:3px}
.partner-badge--round{width:34px;height:34px;border-radius:50%}

/* Services */
.section-title{text-align:center;color:var(--ink);font-size:30px}
.services{top:720px;height:460px;background:var(--white)}
.services .section-title{position:absolute;top:86px;width:100%}
.service-list{position:absolute;top:160px;left:150px;right:150px;display:grid;grid-template-columns:repeat(4,1fr);gap:30px;text-align:center}
.service__icon{width:58px;height:58px;margin:0 auto 14px}
.service__name{color:var(--ink);font-size:14px;font-weight:700;margin-bottom:8px}
.service__text{font-size:12px;line-height:18px;color:var(--muted)}
.services .btn{position:absolute;top:370px;left:50%;transform:translateX(-50%);padding:12px 24px;font-size:12px}

/* Background and expertise */
.expertise{top:1180px;height:960px;background:var(--blush)}
.expertise .section-title{position:absolute;top:80px;width:100%;font-size:32px}
.expertise__intro{position:absolute;top:140px;left:190px;right:190px;text-align:center;font-size:12.5px;line-height:21px;color:var(--muted)}
.laptop{position:absolute;top:230px;left:340px;width:520px;height:420px}
.laptop__screen{position:absolute;left:36px;top:0;width:448px;height:300px;background:#222;border-radius:14px;padding:14px}
.laptop__display{width:100%;height:100%;background:linear-gradient(180deg,#4aa0d8,#1f6aa8)}
.laptop__base{position:absolute;left:0;top:300px;width:520px;height:18px;background:linear-gradient(#d7d9dc,#9ea2a7);border-radius:0 0 40px 40px}
.engagement-title{position:absolute;top:700px;width:100%;text-align:center;color:var(--ink);font-size:21px}
.engagement{position:absolute;top:748px;left:200px;right:200px;display:grid;grid-template-columns:1fr 1fr;column-gap:80px;row-gap:34px}
.model{display:flex;gap:14px}
.model__icon{flex:0 0 26px;height:26px}
.model__name{color:var(--ink);font-size:12.5px;font-weight:700;text-transform:uppercase;margin-bottom:4px}
.model__text{font-size:12px;line-height:18px;color:var(--muted)}

/* Case studies */
.cases{top:2140px;height:320px;background:linear-gradient(180deg,#f4f5f6 0%,#d9dcdf 55%,#eceef0 100%);overflow:hidden}
.cases .section-title{position:absolute;top:56px;width:100%;font-size:26px}
.cases__sub{position:absolute;top:96px;width:100%;text-align:center;font-size:13px;color:var(--text)}
.case-list{position:absolute;top:140px;left:190px;right:190px;display:grid;grid-template-columns:1fr 1fr;gap:56px}
.case{display:flex;background:var(--white);height:132px;box-shadow:0 3px 10px rgba(0,0,0,.12)}
.case__image{flex:0 0 130px;background:linear-gradient(135deg,#3b78b5,#1c3c62)}
.case__body{padding:14px 16px}
.case__title{color:var(--ink);font-size:14px;font-weight:700;margin-bottom:6px}
.case__text{font-size:11.5px;line-height:17px;color:var(--muted)}

/* Newsletter */
.newsletter{top:2460px;height:140px;background:#f2f2f3;display:flex;align-items:center;padding:0 190px;gap:60px}
.newsletter__title{color:var(--ink);font-size:22px;white-space:nowrap}
.newsletter__form{flex:1;display:flex;align-items:center;border-bottom:1px solid #c9ccd0;height:44px;background:var(--white);padding:0 14px}
.newsletter__input{flex:1;font-size:12px;color:var(--muted)}

/* Footer */
.site-footer{top:2600px;height:330px;background:var(--footer);color:#b8bbc0}
.footer-cols{position:absolute;top:40px;left:160px;right:160px;display:grid;grid-template-columns:220px 1fr 260px;gap:40px}
.footer-heading{color:var(--white);font-size:14px;font-weight:700;margin-bottom:16px}
.footer-links li{list-style:none;font-size:12px;line-height:23px}
.blog{display:flex;gap:14px;margin-bottom:16px}
.blog__thumb{flex:0 0 74px;height:48px;background:linear-gradient(135deg,#4d5a68,#252c35)}
.blog__title{color:var(--white);font-size:12px;font-weight:700;text-transform:uppercase}
.blog__text{font-size:11px;line-height:16px}
.contact li{list-style:none;display:flex;gap:10px;font-size:12px;line-height:18px;margin-bottom:10px}
.contact svg{flex:0 0 14px;margin-top:2px}
.social{display:flex;gap:8px;margin-top:8px}
.social span{width:26px;height:26px;background:var(--blue)}
.copyright{position:absolute;top:2930px;left:0;width:1200px;height:30px;background:var(--red);color:var(--white);font-size:11px;text-align:center;line-height:30px}
</style>
</head>
<body>

<header class="hero">
  <div class="hero__image" role="img" aria-label="Dark photograph of glass office towers seen from below"></div>
  <nav class="nav">
    <div class="brand"><span class="brand__mark"></span>BRIVOLT</div>
    <div class="menu-toggle" aria-label="Menu"><span></span><span></span><span></span></div>
  </nav>
  <h1 class="hero__title display">Make Your<br>Product Happen</h1>
  <p class="hero__lead">You need a software product development partner for whom product development is not just a project</p>
  <a class="btn">Driven by Architecture</a>
  <svg class="play" viewBox="0 0 86 86" aria-label="Play video">
    <circle cx="43" cy="43" r="40" fill="none" stroke="var(--red)" stroke-width="4"/>
    <path d="M35 28 L60 43 L35 58 Z" fill="var(--red)"/>
  </svg>
  <div class="partners">
    <p class="partners__text">OUR PARTNERS - WE ARE TRUSTED BY GROWING PRODUCT TEAMS</p>
    <div class="partners__logos">
      <span class="partner-badge"></span>
      <span class="partner-badge partner-badge--round"></span>
      <span class="partner-badge"></span>
      <span class="partner-badge"></span>
    </div>
  </div>
</header>

<section class="services">
  <h2 class="section-title display">Brivolt Services</h2>
  <div class="service-list">
    <div class="service">
      <svg class="service__icon" viewBox="0 0 58 58"><circle cx="29" cy="29" r="27" fill="none" stroke="var(--teal)" stroke-width="2.5"/><circle cx="29" cy="25" r="9" fill="none" stroke="var(--ink)" stroke-width="2"/><path d="M25 36h8M26 40h6" stroke="var(--ink)" stroke-width="2"/></svg>
      <h3 class="service__name">R&amp;D</h3>
      <p class="service__text">Whether it is a simple or new app prototype, or a more complex POC prototype.</p>
    </div>
    <div class="service">
      <svg class="service__icon" viewBox="0 0 58 58"><circle cx="29" cy="29" r="27" fill="none" stroke="var(--teal)" stroke-width="2.5"/><circle cx="29" cy="29" r="8" fill="none" stroke="var(--ink)" stroke-width="2"/><path d="M29 15v6M29 37v6M15 29h6M37 29h6M19 19l4 4M35 35l4 4M39 19l-4 4M23 35l-4 4" stroke="var(--ink)" stroke-width="2"/></svg>
      <h3 class="service__name">Build Products</h3>
      <p class="service__text">Your team of product design thinkers and engineers work with everyone you need to ship and scale a product.</p>
    </div>
    <div class="service">
      <svg class="service__icon" viewBox="0 0 58 58"><circle cx="29" cy="29" r="27" fill="none" stroke="var(--green)" stroke-width="2.5"/><path d="M20 38l12-12M32 26a6 6 0 1 0 4-8l-4 4 2 2 4-4" fill="none" stroke="var(--ink)" stroke-width="2.4"/></svg>
      <h3 class="service__name">Maintain Products</h3>
      <p class="service__text">We have the ability to quickly understand legacy products, make updates and support across teams.</p>
    </div>
    <div class="service">
      <svg class="service__icon" viewBox="0 0 58 58"><circle cx="29" cy="29" r="27" fill="none" stroke="var(--ink)" stroke-width="2.5"/><rect x="18" y="20" width="22" height="15" fill="none" stroke="var(--ink)" stroke-width="2"/><path d="M24 40h10M29 35v5" stroke="var(--ink)" stroke-width="2"/></svg>
      <h3 class="service__name">ODC Setup</h3>
      <p class="service__text">We help in setting up Offshore Development Centres for small and medium software companies at a cost.</p>
    </div>
  </div>
  <a class="btn">View More Services</a>
</section>

<section class="expertise">
  <h2 class="section-title display">Background and Expertise</h2>
  <p class="expertise__intro">We are primarily senior tech engineers with expertise in large scale projects. The Brivolt Software team builds Service Oriented Architecture and cloud systems for product companies. Over the years we have been the trusted offshore product development partner for many startups and for small software businesses across regions.</p>
  <div class="laptop">
    <div class="laptop__screen"><div class="laptop__display" role="img" aria-label="Illustration of a service oriented architecture diagram with platform, people and process icons on a blue screen"></div></div>
    <div class="laptop__base"></div>
  </div>
  <h3 class="engagement-title display">Engagement Models</h3>
  <div class="engagement">
    <div class="model">
      <svg class="model__icon" viewBox="0 0 26 26"><circle cx="13" cy="13" r="11" fill="none" stroke="var(--red)" stroke-width="2"/><path d="M8 13l4 4 6-8" fill="none" stroke="var(--red)" stroke-width="2"/></svg>
      <div><h4 class="model__name">CPO</h4><p class="model__text">We provide a full product team that takes ownership of the entire product development lifecycle.</p></div>
    </div>
    <div class="model">
      <svg class="model__icon" viewBox="0 0 26 26"><circle cx="13" cy="13" r="11" fill="none" stroke="var(--red)" stroke-width="2"/><path d="M9 13h9M14 9l4 4-4 4" fill="none" stroke="var(--red)" stroke-width="2"/></svg>
      <div><h4 class="model__name">Exit</h4><p class="model__text">We help in setting up a team to take global expertise to your product and then grow the team.</p></div>
    </div>
    <div class="model">
      <svg class="model__icon" viewBox="0 0 26 26"><circle cx="13" cy="13" r="11" fill="none" stroke="var(--red)" stroke-width="2"/><path d="M13 7v12M9 11h8" fill="none" stroke="var(--red)" stroke-width="2"/></svg>
      <div><h4 class="model__name">Equity Based</h4><p class="model__text">If you are a startup with very strong growth potential, we are interested. We can build with you.</p></div>
    </div>
    <div class="model">
      <svg class="model__icon" viewBox="0 0 26 26"><circle cx="13" cy="13" r="11" fill="none" stroke="var(--red)" stroke-width="2"/><rect x="8" y="8" width="10" height="10" fill="none" stroke="var(--red)" stroke-width="2"/></svg>
      <div><h4 class="model__name">Architectural and Process Consultancy</h4><p class="model__text">Architecture and process reviews that help your teams build better, faster products.</p></div>
    </div>
  </div>
</section>

<section class="cases" role="img" aria-label="Faded photograph of a bright modern office interior">
  <h2 class="section-title display">Case Studies</h2>
  <p class="cases__sub">Brivolt Case Studies</p>
  <div class="case-list">
    <article class="case">
      <div class="case__image" role="img" aria-label="Photo of a team reviewing a product on screen"></div>
      <div class="case__body">
        <h3 class="case__title">Automation For Your New Product...</h3>
        <p class="case__text">Built a complete automation suite for a product team. It now runs its releases in hours, with test coverage across every module and less manual work.</p>
      </div>
    </article>
    <article class="case">
      <div class="case__image" role="img" aria-label="Photo of server racks in a data center"></div>
      <div class="case__body">
        <h3 class="case__title">Data Center Asset Tracking Product...</h3>
        <p class="case__text">An asset tracking product that gives operators a live view of every rack, device and license across multiple data centers, with alerts and reports.</p>
      </div>
    </article>
  </div>
</section>

<section class="newsletter">
  <h2 class="newsletter__title display">Newsletter Signup Here</h2>
  <div class="newsletter__form">
    <span class="newsletter__input">Enter Your Email</span>
    <svg width="20" height="20" viewBox="0 0 20 20" aria-label="Send"><path d="M2 10L18 2 14 18 10 11Z" fill="var(--ink)"/></svg>
  </div>
</section>

<footer class="site-footer">
  <div class="footer-cols">
    <div>
      <h4 class="footer-heading">Quick Links</h4>
      <ul class="footer-links"><li>Home</li><li>Services</li><li>About Us</li><li>Engagement</li><li>Case Studies</li><li>Blog</li><li>Contact Us</li></ul>
    </div>
    <div>
      <h4 class="footer-heading">Recent Blogs</h4>
      <div class="blog"><div class="blog__thumb" role="img" aria-label="Blog thumbnail photo"></div><div><p class="blog__title">Connected Workflows Built...</p><p class="blog__text">A short look at how product teams ship<br>faster with shared pipelines.</p></div></div>
      <div class="blog"><div class="blog__thumb" role="img" aria-label="Blog thumbnail photo"></div><div><p class="blog__title">Connected Workflows Built...</p><p class="blog__text">A short look at how product teams ship<br>faster with shared pipelines.</p></div></div>
      <div class="blog"><div class="blog__thumb" role="img" aria-label="Blog thumbnail photo"></div><div><p class="blog__title">Connected Workflows Built...</p><p class="blog__text">A short look at how product teams ship<br>faster with shared pipelines.</p></div></div>
    </div>
    <div>
      <h4 class="footer-heading">Contact Us</h4>
      <ul class="contact">
        <li><svg viewBox="0 0 14 14" width="14" height="14"><path d="M7 1a4 4 0 0 0-4 4c0 3 4 8 4 8s4-5 4-8a4 4 0 0 0-4-4z" fill="var(--red)"/></svg><span>Brivolt Software, 12 Harbor Lane,<br>Suite 40, Lakeview 560001</span></li>
        <li><svg viewBox="0 0 14 14" width="14" height="14"><path d="M3 1l3 3-2 2a8 8 0 0 0 4 4l2-2 3 3-2 2C6 13 1 8 1 3z" fill="var(--red)"/></svg><span>+00 555 0142 880</span></li>
        <li><svg viewBox="0 0 14 14" width="14" height="14"><rect x="1" y="3" width="12" height="8" fill="none" stroke="var(--red)" stroke-width="1.5"/><path d="M1 3l6 5 6-5" fill="none" stroke="var(--red)" stroke-width="1.5"/></svg><span>hello@brivoltsoftware-example.com</span></li>
      </ul>
      <div class="social"><span></span><span></span><span></span><span></span></div>
    </div>
  </div>
</footer>
<p class="copyright">© Copyright 2017 Brivolt Software. All Rights are Reserved.</p>

</body>
</html>
```